KRT Civils*

we are a construction company specialising in Housing, Water Infrastructure and Roadworks
This is the description I would like to be added to the Flyer. I have
also attached a Picture
Krt Civils is a Construction Company specializing in Housing, Roadworks
and Water infrastructure. Krt has established itself firmly in the
Construction industry with branches all through Southern Africa as well
as into Africa.
Krt is committed to giving its Clients efficient and Professional
service at all times, We pride ourselves on our ability to meet
deadlines and exceed expectations. Our aim is to establish Successful
Long lasting relationships with our Client base
Colors
Designer to choose only greyscale colors for use in the design.
Look and feel

```html
<!DOCTYPE html>
<html lang="en">
<head>
<meta charset="utf-8">
<title>Krt Civils Flyer</title>
<link rel="stylesheet" href="https://fonts.googleapis.com/css2?family=Lato:wght@400;700;900&display=swap">
<style>
  :root {
    --ink: #1d1d1d;
    --band: #333333;
    --panel: #202020;
    --paper: #ffffff;
    --hex: #f4f4f4;
    --photo-light: #b9b9b9;
    --photo-mid: #8a8a8a;
    --photo-dark: #5e5e5e;
    --figure: #9a9a9a;
  }
  * { margin: 0; padding: 0; box-sizing: border-box; }
  html, body { width: 848px; height: 1200px; overflow: hidden; background: var(--paper); }
  body { font-family: "Lato", sans-serif; color: var(--ink); }
  .flyer { position: relative; width: 848px; height: 1200px; overflow: hidden; background: var(--paper); }
  .hero { position: absolute; left: 0; top: 0; width: 848px; height: 660px; }
  .brand {
    position: absolute; left: 556px; top: 55px;
    display: flex; align-items: center; gap: 10px;
    font-weight: 900; font-size: 30px; letter-spacing: 1px; color: var(--ink);
  }
  .brand-square { width: 22px; height: 22px; background: var(--ink); }
  .specialization { position: absolute; left: 32px; top: 453px; width: 371px; height: 294px; }
  .panel-shape { position: absolute; left: 0; top: 0; }
  .spec-title {
    position: absolute; left: 19px; top: 50px;
    color: var(--paper); font-weight: 700; font-size: 32px; line-height: 40px;
  }
  .services { position: absolute; left: 0; top: 146px; width: 371px; height: 130px; }
  .service {
    position: absolute; top: 0; width: 120px; text-align: center;
    color: var(--paper); font-size: 16px; font-weight: 400; line-height: 20px;
  }
  .service-icon { display: block; margin: 0 auto 9px; }
  .intro {
    position: absolute; left: 444px; top: 664px; width: 400px;
    font-size: 18px; font-weight: 700; line-height: 27px; letter-spacing: 0.8px; color: var(--ink);
  }
  .commitment-head {
    position: absolute; left: 0; top: 818px; width: 848px; height: 56px;
    background: var(--panel);
  }
  .commitment-head h2 {
    position: absolute; left: 33px; top: 8px;
    color: var(--paper); font-size: 32px; font-weight: 700; letter-spacing: 0.2px;
  }
  .commitments { position: absolute; left: 0; top: 874px; width: 686px; height: 269px; background: var(--paper); }
  .connector { position: absolute; left: 0; top: 0; }
  .pledge { position: absolute; font-size: 21px; font-weight: 700; line-height: 27px; color: var(--ink); }
  .figure-column { position: absolute; left: 686px; top: 874px; width: 162px; height: 269px; background: var(--panel); }
  .figure {
    position: absolute; left: 28px; top: 0; width: 100px; height: 260px;
    background: linear-gradient(180deg, var(--figure), #7d7d7d);
    border-radius: 40px 40px 8px 8px;
  }
  .footer {
    position: absolute; left: 0; top: 1143px; width: 848px; height: 57px;
    background: var(--panel); color: var(--paper);
    font-size: 14px; font-weight: 700; letter-spacing: 0.6px;
  }
  .footer span { position: absolute; top: 20px; }
  .footer .phone { left: 32px; }
  .footer .web { left: 349px; }
  .footer .mail { right: 18px; top: 17px; }
</style>
</head>
<body>
<main class="flyer">
  <svg class="hero" viewBox="0 0 848 660" width="848" height="660">
    <defs>
      <linearGradient id="photoTone" x1="0" y1="0" x2="0" y2="1">
        <stop offset="0" stop-color="var(--photo-light)"/>
        <stop offset="0.45" stop-color="var(--photo-mid)"/>
        <stop offset="1" stop-color="var(--photo-dark)"/>
      </linearGradient>
    </defs>
    <path class="hero-band" fill="var(--band)"
      d="M0,0 L152,0 L848,232 L848,450 C800,560 720,648 620,640 C560,636 500,610 440,585 L0,425 Z"/>
    <path class="hero-photo" fill="url(#photoTone)" role="img"
      aria-label="Photograph of a new housing development with rows of small houses and power poles"
      d="M10,0 L848,286 L848,418 C800,520 720,610 615,604 C560,600 505,578 450,556 L0,392 L0,35 Z"/>
  </svg>

  <div class="brand"><span class="brand-square"></span>KRT Civils</div>

  <section class="specialization">
    <svg class="panel-shape" viewBox="0 0 371 294" width="371" height="294">
      <path fill="var(--panel)" d="M0,0 L371,127 L371,276 Q371,294 350,294 L0,294 Z"/>
    </svg>
    <h1 class="spec-title">Krt<br>Specialization</h1>
    <div class="services">
      <div class="service" style="left:-1px">
        <svg class="service-icon" width="80" height="67" viewBox="0 0 80 67">
          <polygon fill="var(--hex)" points="20,0 60,0 80,33.5 60,67 20,67 0,33.5"/>
          <path fill="var(--ink)" d="M40,17 L59,34 L54,34 L54,50 L45,50 L45,40 L35,40 L35,50 L26,50 L26,34 L21,34 Z"/>
        </svg>Housing
      </div>
      <div class="service" style="left:119px">
        <svg class="service-icon" width="80" height="67" viewBox="0 0 80 67">
          <polygon fill="var(--hex)" points="20,0 60,0 80,33.5 60,67 20,67 0,33.5"/>
          <path fill="var(--ink)" d="M36,16 L44,16 L51,46 L29,46 Z"/>
          <rect fill="var(--hex)" x="32" y="26" width="16" height="4"/>
          <rect fill="var(--hex)" x="30" y="35" width="20" height="4"/>
          <rect fill="var(--ink)" x="24" y="46" width="32" height="5"/>
        </svg>Roadworks
      </div>
      <div class="service" style="left:238px">
        <svg class="service-icon" width="80" height="67" viewBox="0 0 80 67">
          <polygon fill="var(--hex)" points="20,0 60,0 80,33.5 60,67 20,67 0,33.5"/>
          <path fill="var(--ink)" d="M33,22 A7,6 0 0 1 47,22 L47,24 L33,24 Z"/>
          <rect fill="var(--ink)" x="34" y="25" width="12" height="24"/>
          <rect fill="var(--ink)" x="29" y="31" width="22" height="7"/>
          <rect fill="var(--ink)" x="31" y="49" width="18" height="4"/>
        </svg>Water<br>infrastructure
      </div>
    </div>
  </section>

  <p class="intro">Krt has established itself firmly in the<br>Construction industry with branches all<br>through Southern Africa as well as into<br>Africa.</p>

  <header class="commitment-head"><h2>Krt is committed to giving its Clients</h2></header>

  <section class="commitments">
    <svg class="connector" viewBox="0 0 686 269" width="686" height="269">
      <g fill="var(--ink)">
        <rect x="82" y="0" width="8" height="215"/>
        <rect x="82" y="33" width="30" height="8"/>
        <polygon points="110,26 133,37 110,48 116,37"/>
        <rect x="82" y="107" width="30" height="8"/>
        <polygon points="110,100 133,111 110,122 116,111"/>
        <rect x="82" y="199" width="30" height="8"/>
        <polygon points="110,192 133,203 110,214 116,203"/>
      </g>
    </svg>
    <p class="pledge" style="left:138px; top:23px">Efficient and Professional service at all times</p>
    <p class="pledge" style="left:144px; top:85px">We pride ourselves on our ability to meet<br>deadlines and exceed expectations.</p>
    <p class="pledge" style="left:144px; top:177px">Our aim is to establish Successful<br>Long lasting relationships with our Client base</p>
  </section>

  <aside class="figure-column">
    <div class="figure" role="img" aria-label="Silhouette of a construction worker holding plans"></div>
  </aside>

  <footer class="footer">
    <span class="phone">Contact: 0110 555 0192</span>
    <span class="web">Website : krtcivils.com</span>
    <span class="mail">Email: info@krtcivils.com</span>
  </footer>
</main>
</body>
</html>
```